New Flyer Design Project - for sale units at The Lodge phase 3

on attached the A2 is full kitchen 1 bedroom, the A3 is gally kitchen and the B2 is the the 2 bedroom, on attached pictures the room with 2 queen beds is only for the 2 bedroom

This is going to be used to sale the units (real estate sale) so the layout could possibly be text and then pictures maybe 1 bedroom on one side and 2 on the back?

Experience the Modern Luxury of the New Phase 3 Building of the
Lodge at Harlow Bend

* Opening Spring 2019

* America's #17 Family Resort; Tennessee's Only Ranked Resort

1 Bedroom Bunk Suite (Galley Kitchen) - $199,000; Sleeps 6

* Private King Master Bedroom

* Bunk Bed Galley

* Granite Counters Throughout

* Fully Furnished with Custom Furnishings

* Private Balcony

* Equipped Galley Kitchen

* In Unit Laundry

* Queen Sleeper Sofa

1 Bedroom Bunk Suite (Full Kitchen) - $209,000; Sleeps 6

* Bunk Bed Galley

* Granite Counters throughout

* Equipped Full Kitchen

* Completely Furnished with Custom Furnishings

* Private Balcony

* In Unit Laundry

* Queen Sleeper Sofa

2 Bedroom Bunk Suite (Full Kitchen) - $249,000; Sleeps 10

* Private King Master Bedroom with On-Suite Bathroom

* Two Queen Bedroom

* Bunk Bed Galley

* Full Kitchen

* Private Balcony

* In Unit Laundry

* Queen Sleeper Sofa

Target Market(s)

people wanting to buy units in phase 3 of The Lodge at Harlow Bend

Industry/Entity Type

Real Estate Development

Requirements
Must have
• attached text to describe units and price
• pictures and layouts
• Contact Dale Porter
• 865-730-2958 Dale@brightfernretreats.example
Nice to have
• brand and logo
Should not have
• it should not be plain this is m ore of a luxury project

```html
<!DOCTYPE html>
<html lang="en">
<head>
<meta charset="utf-8">
<title>The Lodge at Harlow Bend – Phase 3 Sales Flyer</title>
<link rel="stylesheet" href="https://fonts.googleapis.com/css2?family=Oswald:wght@500;600&family=Roboto+Condensed:wght@400;700&family=Roboto:wght@400;500&display=swap">
<style>
:root{
  --navy:#232f8f;
  --navy-deep:#1a2370;
  --gold:#c8904a;
  --gold-light:#e2b77c;
  --grey-line:#b9bcc6;
  --ink:#2b2b35;
  --paper:#ffffff;
  --backdrop:#e6e7ea;
}
*{box-sizing:border-box;margin:0;padding:0}
html,body{width:788px;height:1200px;overflow:hidden}
body{background:var(--backdrop);position:relative;font-family:'Roboto',Arial,sans-serif;color:var(--ink)}
.flyer{position:absolute;left:194px;width:400px;height:566px;background:var(--paper);overflow:hidden;box-shadow:0 2px 8px rgba(0,0,0,.18)}
.flyer--front{top:22px}
.flyer--back{top:610px}
.photo{position:absolute;left:0;width:100%}
.flyer--front .photo--hero{top:0;height:310px;background:linear-gradient(180deg,#2b3a86 0%,#5e6a90 26%,#6b5846 48%,#d8d3cb 66%,#a07a55 100%)}
.flyer--back .photo--hero{top:0;height:270px;background:linear-gradient(160deg,#e8eadf 0%,#c9cfae 30%,#8e9e6e 50%,#f1efe8 70%,#d9c99e 100%)}
.header{position:absolute;left:0;top:0;width:100%;height:104px;background:linear-gradient(180deg,var(--navy) 0%,rgba(35,47,143,.85) 60%,rgba(35,47,143,0) 100%);text-align:center;color:#fff}
.header__title{font-family:'Oswald',sans-serif;font-weight:500;font-size:34px;letter-spacing:.5px;line-height:1;padding-top:12px}
.header__ribbon{display:inline-block;margin-top:4px;background:linear-gradient(90deg,#a8743a,var(--gold-light) 50%,#a8743a);font-family:'Roboto Condensed',sans-serif;font-weight:700;font-size:11px;padding:2px 10px;color:#fff}
.header__intro{font-size:10px;line-height:12px;margin-top:3px;padding:0 40px}
.swoosh{position:absolute;left:0;top:0;width:400px;height:566px}
.porthole{position:absolute;border-radius:50%;border:3px solid #fff;box-shadow:0 0 0 2px var(--navy)}
.porthole--dining{left:22px;top:216px;width:96px;height:96px;background:radial-gradient(circle at 40% 40%,#f0efe9,#8a8f9a 70%,#3b3c44)}
.porthole--bedroom{left:128px;top:204px;width:82px;height:82px;background:radial-gradient(circle at 50% 55%,#fafafa,#c2b9a8 60%,#6b6a70)}
.porthole--bath{left:224px;top:164px;width:64px;height:64px;background:radial-gradient(circle at 50% 50%,#ece9e2,#a89f90 70%,#4f4c4a)}
.brand{position:absolute;font-family:'Roboto Condensed',sans-serif;font-weight:700;color:var(--gold);text-align:center;line-height:1.05;display:flex;align-items:center;gap:6px}
.brand__mark{width:10px;height:10px;background:var(--gold);flex:none}
.flyer--front .brand{left:256px;top:250px;font-size:16px;width:130px;justify-content:center}
.flyer--back .brand{left:130px;top:252px;font-size:18px;width:140px;justify-content:center}
.unit{position:absolute;left:12px}
.unit__title{font-family:'Roboto Condensed',sans-serif;font-weight:700;font-size:11px;color:var(--navy);white-space:nowrap}
.unit__title .price{color:var(--gold)}
.unit__title .sep{color:var(--navy);font-weight:400}
.unit__title .kitchen{font-weight:400}
.unit__features{display:flex;gap:10px;margin-top:8px}
.unit__features ul{list-style:none}
.unit__features li{font-size:7.5px;line-height:12px;color:var(--ink);padding-left:10px;position:relative;white-space:nowrap}
.unit__features li::before{content:"";position:absolute;left:1px;top:3px;width:5px;height:3px;border-left:1.2px solid var(--navy);border-bottom:1.2px solid var(--navy);transform:rotate(-45deg)}
.col-a{width:152px}
.floorplan{position:absolute;border:1px solid #9aa0ab;background:linear-gradient(135deg,#efe9dc,#d9cdb4 45%,#e8e2d4 70%,#2f63a8 71%,#2f63a8 78%,#e3dccc 79%)}
.flyer--front .unit--galley{top:324px}
.flyer--front .unit--full{top:408px}
.flyer--front .floorplan--galley{left:296px;top:324px;width:94px;height:66px}
.flyer--front .floorplan--full{left:296px;top:406px;width:90px;height:84px}
.flyer--back .unit--two{top:338px}
.flyer--back .unit--two .unit__features li{line-height:12.8px}
.flyer--back .floorplan--two{left:246px;top:360px;width:140px;height:160px}
.site{position:absolute;left:32px;bottom:9px;font-size:8.5px;color:#fff;letter-spacing:.1px}
.contact{position:absolute;right:14px;bottom:6px;font-size:7px;line-height:9px;color:#fff;text-align:right}
.contact__name{font-weight:500}
</style>
</head>
<body>

<section class="flyer flyer--front">
  <div class="photo photo--hero" role="img" aria-label="Photo of a modern suite bedroom with a king bed, dark headboard wall and open bathroom"></div>
  <header class="header">
    <h1 class="header__title">OPENING SPRING 2019</h1>
    <p class="header__ribbon">America's #17 Family Resort; Tennessee's Only Ranked Resort</p>
    <p class="header__intro">Experience the Modern Luxury of the New Phase3 Building of the Lodge at Harlow Bend</p>
  </header>
  <svg class="swoosh" viewBox="0 0 400 566" aria-hidden="true">
    <path d="M0 290 C110 290 250 250 400 170 L400 566 L0 566Z" fill="#ffffff"/>
    <path d="M0 250 C120 238 260 198 400 158 L400 188 C270 238 130 288 0 300Z" fill="#232f8f"/>
    <path d="M110 252 C220 234 320 198 400 170" fill="none" stroke="#c8904a" stroke-width="5"/>
    <path d="M0 300 C130 288 270 238 400 188" fill="none" stroke="#ffffff" stroke-width="2"/>
    <path d="M0 524 C140 500 280 532 400 510" fill="none" stroke="#b9bcc6" stroke-width="3"/>
    <path d="M0 532 C140 508 280 540 400 518" fill="none" stroke="#c8904a" stroke-width="3"/>
    <path d="M0 540 C140 516 280 546 400 524 L400 566 L0 566Z" fill="#232f8f"/>
  </svg>
  <div class="porthole porthole--dining" role="img" aria-label="Photo of dining area with granite counter"></div>
  <div class="porthole porthole--bedroom" role="img" aria-label="Photo of bedroom with bed and lamp"></div>
  <div class="porthole porthole--bath" role="img" aria-label="Photo of bathroom vanity"></div>
  <div class="brand"><span class="brand__mark"></span><span>The Lodge<br>at Harlow Bend</span></div>

  <article class="unit unit--galley">
    <h2 class="unit__title">1 Bedroom Bunk Suite (Galley Kitchen) <span class="sep">|</span> <span class="price">$199,000</span> <span class="sep">|</span> Sleeps 6</h2>
    <div class="unit__features">
      <ul class="col-a">
        <li>Private King Master Bedroom</li>
        <li>Bunk Bed Galley</li>
        <li>Granite Counters Throughout</li>
        <li>Fully Furnished with Custom Furnishings</li>
      </ul>
      <ul>
        <li>Private Balcony</li>
        <li>Equipped Galley Kitchen</li>
        <li>In Unit Laundry</li>
        <li>Queen Sleeper Sofa</li>
      </ul>
    </div>
  </article>
  <div class="floorplan floorplan--galley" role="img" aria-label="Floor plan of the 1 bedroom galley kitchen suite"></div>

  <article class="unit unit--full">
    <h2 class="unit__title">1 Bedroom Bunk Suite <span class="kitchen">(Full Kitchen)</span> <span class="sep">|</span> <span class="price">$209,000</span> <span class="sep">|</span> Sleeps 6</h2>
    <div class="unit__features">
      <ul class="col-a">
        <li>Private King Master Bedroom</li>
        <li>Bunk Bed Galley</li>
        <li>Granite Counters throughout</li>
        <li>Equipped Full Kitchen</li>
      </ul>
      <ul>
        <li>Completely Furnished with<br>Custom Furnishings</li>
        <li>Private Balcony</li>
        <li>In Unit Laundry</li>
        <li>Queen Sleeper Sofa</li>
      </ul>
    </div>
  </article>
  <div class="floorplan floorplan--full" role="img" aria-label="Floor plan of the 1 bedroom full kitchen suite"></div>

  <p class="site">www.brightfernretreats.example</p>
  <p class="contact"><span class="contact__name">Contact Dale Porter</span> | 865-730-2958<br>Dale@brightfernretreats.example</p>
</section>

<section class="flyer flyer--back">
  <div class="photo photo--hero" role="img" aria-label="Photo of a bedroom with two queen beds, green wall and window with curtains"></div>
  <svg class="swoosh" viewBox="0 0 400 566" aria-hidden="true">
    <path d="M0 250 C90 200 200 260 400 230 L400 566 L0 566Z" fill="#ffffff"/>
    <path d="M0 190 C70 230 120 245 220 235 C300 228 360 215 400 205 L400 232 C330 258 240 268 160 272 C90 275 40 262 0 250Z" fill="#232f8f"/>
    <path d="M0 186 C70 226 130 240 220 231 C300 224 360 212 400 201" fill="none" stroke="#c8904a" stroke-width="4"/>
    <path d="M0 250 C50 264 110 276 170 273 C250 268 330 258 400 232" fill="none" stroke="#c8904a" stroke-width="2"/>
    <path d="M0 524 C140 500 280 532 400 510" fill="none" stroke="#b9bcc6" stroke-width="3"/>
    <path d="M0 532 C140 508 280 540 400 518" fill="none" stroke="#c8904a" stroke-width="3"/>
    <path d="M0 540 C140 516 280 546 400 524 L400 566 L0 566Z" fill="#232f8f"/>
  </svg>
  <div class="brand"><span class="brand__mark"></span><span>The Lodge<br>at Harlow Bend</span></div>

  <article class="unit unit--two">
    <h2 class="unit__title">2 Bedroom Bunk Suite (Full Kitchen) <span class="sep">|</span> <span class="price">$249,000</span> <span class="sep">|</span> Sleeps 10</h2>
    <div class="unit__features">
      <ul>
        <li>Private King Master Bedroom with On-Suite Bathroom</li>
        <li>Two Queen Bedroom</li>
        <li>Bunk Bed Galley</li>
        <li>Granite Counters Throughout</li>
        <li>Full Kitchen</li>
        <li>Completely Furnished with Custom Furnishings</li>
        <li>Private Balcony</li>
        <li>In Unit Laundry</li>
        <li>Queen Sleeper Sofa</li>
      </ul>
    </div>
  </article>
  <div class="floorplan floorplan--two" role="img" aria-label="Floor plan of the 2 bedroom full kitchen suite"></div>

  <p class="site">www.brightfernretreats.example</p>
  <p class="contact"><span class="contact__name">Contact Dale Porter</span> | 865-730-2958<br>Dale@brightfernretreats.example</p>
</section>

</body>
</html>
```